Wageline Associates Business Card Design

We need a business card designed around our new logo. The business card should be modern in design & should communicate success, confidence, power, sophistication. The target market is young business professionals. This is for a human resource & payroll outsourcing business.

```html
<!DOCTYPE html>
<html lang="en">
<head>
<meta charset="utf-8">
<title>Wageline Associates Business Card</title>
<link rel="stylesheet" href="https://fonts.googleapis.com/css2?family=Tinos:ital,wght@0,400;1,400;1,700&display=swap">
<style>
  :root {
    --backdrop: #1c1c1c;
    --card: #ffffff;
    --ink: #111111;
    --red: #e41f26;
    --red-deep: #c4262d;
    --white: #ffffff;
  }
  * { box-sizing: border-box; margin: 0; padding: 0; }
  html, body {
    width: 900px; height: 1200px; overflow: hidden;
    background: var(--backdrop);
    font-family: "Tinos", "Times New Roman", serif;
  }
  .canvas { position: relative; width: 900px; height: 1200px; }
  .card {
    position: absolute; left: 80px; width: 733px; height: 428px;
    background: var(--card); border-radius: 22px; overflow: hidden;
  }
  .card--front { top: 128px; }
  .card--back { top: 646px; }

  .holder-name {
    position: absolute; left: 66px; top: 60px;
    font-style: italic; font-weight: 700; font-size: 25px; color: var(--ink);
  }
  .holder-title {
    position: absolute; left: 66px; top: 89px;
    font-style: italic; font-size: 16px; color: var(--red);
  }
  .address {
    position: absolute; left: 66px; top: 172px;
    font-style: italic; font-size: 16.5px; line-height: 22.5px; color: var(--ink);
  }
  .contacts {
    position: absolute; left: 66px; top: 294px; list-style: none;
    font-style: italic; font-size: 16.5px; line-height: 23px; color: var(--ink);
  }
  .contacts li { display: flex; align-items: center; gap: 10px; }
  .contacts svg { width: 15px; height: 15px; fill: var(--red); flex: none; }

  .brand-figure { position: absolute; right: 0; top: 0; width: 250px; height: 428px; }

  .brand-mark {
    position: absolute; left: 0; right: 0; top: 178px;
    display: flex; justify-content: center; align-items: center; gap: 12px;
  }
  .brand-mark__dot { width: 16px; height: 16px; border-radius: 50%; background: var(--red); }
  .brand-mark__name { font-size: 40px; font-weight: 400; color: var(--ink); letter-spacing: 0.3px; }

  .web-band {
    position: absolute; left: 0; right: 0; top: 390px; height: 26px;
    background: var(--red); color: var(--white);
    font-style: italic; font-size: 14.5px; text-align: center; line-height: 26px;
  }
</style>
</head>
<body>
<main class="canvas">
  <section class="card card--front">
    <h1 class="holder-name">Daniel Whitmore</h1>
    <p class="holder-title">Managing Director</p>
    <address class="address">418 Harbor Street<br>Suite 210, Lakeview<br>MI 49021</address>
    <ul class="contacts">
      <li><svg viewBox="0 0 16 16"><path d="M3 1l3 3-1.5 2c1 2 3 4 5 5L11.5 9.5l3 3L13 15C7 15 1 9 1 3z"/></svg>555-014-2290</li>
      <li><svg viewBox="0 0 16 16"><path d="M4 1h8v4H4zM1 6h14v6h-3v3H4v-3H1zM5 10v4h6v-4z"/></svg>555-014-2290</li>
      <li><svg viewBox="0 0 16 16"><path d="M1 3h14v1L8 9 1 4zM1 6l7 5 7-5v7H1z"/></svg>info@wagelineassociates.com</li>
      <li><svg viewBox="0 0 16 16"><circle cx="8" cy="8" r="7"/><path d="M1 8h14M8 1v14M3 4h10M3 12h10" stroke="#fff" stroke-width="1" fill="none"/></svg>www.wagelineassociates.com</li>
    </ul>
    <svg class="brand-figure" viewBox="0 0 250 428" role="img" aria-label="Area for the brand figure decoration in red">
      <defs>
        <linearGradient id="figureTone" x1="0" y1="0" x2="1" y2="1">
          <stop offset="0" stop-color="#e41f26"/>
          <stop offset="1" stop-color="#c4262d"/>
        </linearGradient>
      </defs>
      <rect x="0" y="0" width="250" height="428" fill="url(#figureTone)"/>
    </svg>
  </section>

  <section class="card card--back">
    <div class="brand-mark">
      <span class="brand-mark__dot"></span>
      <span class="brand-mark__name">Wageline Associates</span>
    </div>
    <p class="web-band">www.wagelineassociates.com</p>
  </section>
</main>
</body>
</html>
```